Marrowind & Co Boutique Accommodation & Open Garden

Boutique Accommodation & Open garden; Weddings, Functions & Tours
A 1904 cottage is surrounded by 5 acres of landscaped gardens 3 of which are open to the public.
The many pathways entice it’s visitor to wonder under romantic rose covered arbours leading them to secluded flower filled areas.
The woodlands create a shady haven to rest in, while the pond at the bottom of the garden adds to the peace and tranquility felt by all in this harmonies spellbinding garden.

Open Thursday through Sunday, or by appointment.

I would like to down load my Logo. How do I do this?

Target Market(s)

Affluent

Colors

Designer to choose colors to be used in the design.

Requirements
Must have
• The Logo, Simplistic and classy.
• I am a graphic designer so have high expectations, but no time to do it myself. The design must be good.What to see and when.
Nice to have
• I am after a great design, must be classy must stand out. Not the run of the mill that everyone has.
Should not have
• Colours must complement Logo. Colours as in the saltwater @ narooma and black background with white writing.

```html
<!DOCTYPE html>
<html lang="en">
<head>
<meta charset="utf-8">
<title>Marrowind &amp; Co Gardens – Trifold Brochure</title>
<link rel="stylesheet" href="https://fonts.googleapis.com/css2?family=Cormorant+Garamond:ital,wght@0,400;0,600;1,400&family=Raleway:wght@300;400;500&display=swap">
<style>
  :root {
    --gold: #b39850;
    --gold-deep: #9c8240;
    --band: #d9d8d3;
    --paper: #ffffff;
    --backdrop: #e4e4e2;
    --ink: #4a4a46;
    --ink-soft: #6d6d68;
    --on-gold: #ffffff;
    --rule-on-gold: rgba(255,255,255,0.45);
  }
  * { box-sizing: border-box; margin: 0; padding: 0; }
  html, body { width: 1200px; height: 2402px; overflow: hidden; background: var(--backdrop); }
  body { position: relative; font-family: "Raleway", sans-serif; color: var(--ink); }

  .defs { position: absolute; width: 0; height: 0; }

  .sheet { position: absolute; display: flex; height: 722px; box-shadow: 0 2px 6px rgba(0,0,0,0.12); }
  .sheet--cover { left: 430px; top: 60px; }
  .sheet--outside { left: 90px; top: 842px; }
  .sheet--inside { left: 90px; top: 1624px; }

  .panel { position: relative; width: 340px; height: 722px; overflow: hidden; background: var(--paper); }
  .panel + .panel { border-left: 1px solid rgba(0,0,0,0.06); }
  .panel > svg.art { position: absolute; inset: 0; width: 340px; height: 722px; }

  /* Cover name: plain, single line, one size and weight */
  .brand-name { position: absolute; top: 130px; left: 20px; right: 20px; text-align: center;
    font-family: "Cormorant Garamond", serif; font-weight: 400; font-size: 30px;
    color: var(--on-gold); line-height: 1.2; white-space: nowrap; }
  .pill { position: absolute; left: 36px; right: 36px; height: 32px; border-radius: 16px;
    background: var(--gold); color: var(--on-gold); display: flex; align-items: center; justify-content: center;
    font-size: 13px; letter-spacing: 0.5px; }
  .pill--url { bottom: 28px; }

  /* Headings & copy */
  .heading { font-family: "Cormorant Garamond", serif; font-weight: 600; color: var(--gold); }
  .heading--on-gold { color: var(--on-gold); font-weight: 400; }
  .copy { font-size: 11.5px; line-height: 1.55; font-weight: 300; }
  .copy--on-gold { color: var(--on-gold); }

  /* About panel */
  .about__title { position: absolute; top: 250px; left: 0; right: 0; text-align: center; font-size: 30px; }
  .about__copy { position: absolute; top: 300px; left: 34px; right: 34px; text-align: center; font-size: 12.5px; }

  /* Contact panel */
  .contact__intro { position: absolute; top: 380px; left: 40px; right: 40px; text-align: center; font-size: 13px; line-height: 1.55; color: var(--ink); font-weight: 300; }
  .pill--enquire { top: 490px; left: 28px; right: 28px; font-size: 11.5px; height: 28px; }
  .contact__details { position: absolute; top: 545px; left: 0; right: 0; text-align: center; font-size: 13px; line-height: 1.6; color: var(--ink); font-style: normal; }
  .contact__hours { color: var(--gold); letter-spacing: 1px; font-weight: 500; }

  /* What to see table */
  .season__title { position: absolute; top: 26px; left: 24px; right: 24px; font-size: 30px; }
  .season-table { position: absolute; top: 80px; left: 24px; width: 292px; border-collapse: collapse;
    color: var(--on-gold); font-size: 10.5px; }
  .season-table th { text-align: left; font-weight: 500; padding: 6px 5px; border-bottom: 1px solid var(--on-gold); letter-spacing: 0.5px; }
  .season-table td { padding: 9px 5px; border-bottom: 1px solid var(--rule-on-gold); vertical-align: top; font-weight: 300; line-height: 1.35; }
  .season-table td:first-child { width: 44px; font-weight: 500; }

  /* Feature blocks */
  .feature { position: absolute; left: 22px; right: 22px; }
  .feature__title { font-size: 23px; margin-bottom: 6px; }
  .feature--upper { top: 236px; }
  .feature--lower { top: 588px; }
</style>
</head>
<body>

<svg class="defs" aria-hidden="true">
  <defs>
    <linearGradient id="tone-arbour" x1="0" y1="0" x2="1" y2="1">
      <stop offset="0" stop-color="#8e9a8c"/>
      <stop offset="0.35" stop-color="#4e7a3a"/>
      <stop offset="0.7" stop-color="#6d8f4f"/>
      <stop offset="1" stop-color="#2f5226"/>
    </linearGradient>
    <linearGradient id="tone-garden" x1="0" y1="0" x2="0" y2="1">
      <stop offset="0" stop-color="#c9d3c2"/>
      <stop offset="0.4" stop-color="#5f8a45"/>
      <stop offset="1" stop-color="#2e4f24"/>
    </linearGradient>
    <linearGradient id="tone-woods" x1="0" y1="0" x2="1" y2="1">
      <stop offset="0" stop-color="#355a2a"/>
      <stop offset="1" stop-color="#7c9a5a"/>
    </linearGradient>
    <linearGradient id="tone-blossom" x1="0" y1="0" x2="1" y2="0">
      <stop offset="0" stop-color="#4f7a3b"/>
      <stop offset="0.6" stop-color="#7f9658"/>
      <stop offset="1" stop-color="#b47896"/>
    </linearGradient>
    <linearGradient id="tone-stone" x1="0" y1="0" x2="1" y2="1">
      <stop offset="0" stop-color="#a8a594"/>
      <stop offset="1" stop-color="#5a6f48"/>
    </linearGradient>
  </defs>
</svg>

<!-- Front cover on its own -->
<section class="sheet sheet--cover" aria-label="Brochure front cover">
  <article class="panel cover">
    <svg class="art" viewBox="0 0 340 722">
      <rect width="340" height="722" fill="var(--gold)"/>
      <path d="M0 292 Q170 222 340 292 L340 308 Q170 238 0 308 Z" fill="var(--band)"/>
      <path role="img" aria-label="Photo: rose-covered garden gazebo with lattice arbour" d="M0 308 Q170 238 340 308 L340 722 L0 722 Z" fill="url(#tone-arbour)"/>
    </svg>
    <h1 class="brand-name">Marrowind &amp; Co Gardens</h1>
    <div class="pill pill--url">www.marrowindgardens.com.au</div>
  </article>
</section>

<!-- Outside spread -->
<section class="sheet sheet--outside" aria-label="Brochure outside spread">
  <article class="panel about">
    <svg class="art" viewBox="0 0 340 722">
      <rect width="340" height="722" fill="var(--gold)"/>
      <path role="img" aria-label="Photo: couple walking beneath a leafy garden archway" d="M0 0 H340 V160 Q170 250 0 160 Z" fill="url(#tone-garden)"/>
      <path d="M0 160 Q170 250 340 160 L340 176 Q170 266 0 176 Z" fill="var(--band)"/>
      <rect role="img" aria-label="Photo: cottage among garden beds" x="24" y="572" width="140" height="118" fill="url(#tone-woods)"/>
      <rect role="img" aria-label="Photo: flowering tree beside a garden path" x="176" y="572" width="140" height="118" fill="url(#tone-blossom)"/>
    </svg>
    <h2 class="heading heading--on-gold about__title">About Us</h2>
    <p class="copy copy--on-gold about__copy">A 1904 cottage is surrounded by five acres of landscaped gardens, three of which are open to the public. Winding pathways lead visitors under rose covered arbours to secluded, flower filled corners, shady woodlands and a tranquil pond at the bottom of the garden.</p>
  </article>

  <article class="panel contact">
    <svg class="art" viewBox="0 0 340 722">
      <rect role="img" aria-label="Photo: terraced garden with clipped hedges and tall trees" x="0" y="0" width="340" height="330" fill="url(#tone-garden)"/>
      <path d="M0 300 Q170 200 340 300 L340 722 L0 722 Z" fill="var(--band)"/>
      <path d="M0 312 Q170 212 340 312 L340 722 L0 722 Z" fill="var(--paper)"/>
      <circle role="img" aria-label="Location map" cx="170" cy="300" r="56" fill="#eeeeec" stroke="var(--band)" stroke-width="3"/>
    </svg>
    <p class="contact__intro">Come enjoy and experience Marrowind Gardens time and time again. The spectacular seasonal transformations and new highlights of the gardens ensure there is always new visual pleasure.</p>
    <div class="pill pill--enquire">Call or check below for pricing and availability</div>
    <address class="contact__details">
      Wrenfield Drive<br>
      Larkvale NSW 2999<br>
      ph: 02 4400 0000<br>
      www.marrowindgardens.com.au<br>
      <span class="contact__hours">OPEN 7 DAYS</span>
    </address>
  </article>

  <article class="panel cover">
    <svg class="art" viewBox="0 0 340 722">
      <rect width="340" height="722" fill="var(--gold)"/>
      <path d="M0 292 Q170 222 340 292 L340 308 Q170 238 0 308 Z" fill="var(--band)"/>
      <path role="img" aria-label="Photo: rose-covered garden gazebo with lattice arbour" d="M0 308 Q170 238 340 308 L340 722 L0 722 Z" fill="url(#tone-arbour)"/>
    </svg>
    <h2 class="brand-name">Marrowind &amp; Co Gardens</h2>
    <div class="pill pill--url">www.marrowindgardens.com.au</div>
  </article>
</section>

<!-- Inside spread -->
<section class="sheet sheet--inside" aria-label="Brochure inside spread">
  <article class="panel season">
    <svg class="art" viewBox="0 0 340 722">
      <rect width="340" height="722" fill="var(--gold)"/>
      <rect role="img" aria-label="Photo: stone arch in a woodland garden" x="24" y="586" width="140" height="110" fill="url(#tone-woods)"/>
      <rect role="img" aria-label="Photo: garden seat beneath trees" x="176" y="586" width="140" height="110" fill="url(#tone-stone)"/>
    </svg>
    <h2 class="heading heading--on-gold season__title">What To See &amp; When</h2>
    <table class="season-table">
      <thead><tr><th>Month</th><th>Highlights</th><th>In Flower</th></tr></thead>
      <tbody>
        <tr><td>Sep</td><td>Spring bulbs and blossom</td><td>Daffodils, magnolia</td></tr>
        <tr><td>Oct</td><td>Wisteria walk, bluebells</td><td>Tulips, azaleas</td></tr>
        <tr><td>Nov</td><td>Rose arbours at their peak</td><td>Roses, foxgloves</td></tr>
        <tr><td>Dec</td><td>Summer borders</td><td>Lilies, salvias</td></tr>
        <tr><td>Jan</td><td>Shady woodland walks</td><td>Hydrangeas</td></tr>
        <tr><td>Mar</td><td>Autumn colour begins</td><td>Dahlias, asters</td></tr>
        <tr><td>May</td><td>Maples and golden elms</td><td>Berries, grasses</td></tr>
        <tr><td>Jul</td><td>Winter structure, hedges</td><td>Camellias, hellebores</td></tr>
      </tbody>
    </table>
  </article>

  <article class="panel features">
    <svg class="art" viewBox="0 0 340 722">
      <rect role="img" aria-label="Photo: ivy-covered garden grotto" x="0" y="20" width="340" height="200" fill="url(#tone-woods)"/>
      <circle role="img" aria-label="Photo: white garden urn" cx="282" cy="190" r="34" fill="url(#tone-stone)" stroke="var(--paper)" stroke-width="4"/>
      <rect role="img" aria-label="Photo: flowering cherry over a lush lawn" x="0" y="372" width="340" height="200" fill="url(#tone-blossom)"/>
      <circle role="img" aria-label="Photo: guest bedroom interior" cx="282" cy="542" r="34" fill="#c9c2b2" stroke="var(--paper)" stroke-width="4"/>
    </svg>
    <div class="feature feature--upper">
      <h3 class="heading feature__title">Open Garden</h3>
      <p class="copy">Three of our five acres are open to visitors from Thursday to Sunday. Wander rose covered arbours, quiet woodland paths and flower filled garden rooms at your own pace.</p>
    </div>
    <div class="feature feature--lower">
      <h3 class="heading feature__title">Accommodation</h3>
      <p class="copy">There are just a handful of charming, elegantly designed rooms on offer for guests wishing to stay a night or more amid the gardens, with breakfast served overlooking the lawns.</p>
    </div>
  </article>

  <article class="panel features">
    <svg class="art" viewBox="0 0 340 722">
      <rect role="img" aria-label="Photo: stone steps under a green canopy" x="0" y="20" width="340" height="200" fill="url(#tone-garden)"/>
      <circle role="img" aria-label="Photo: garden archway detail" cx="282" cy="190" r="34" fill="url(#tone-woods)" stroke="var(--paper)" stroke-width="4"/>
      <rect role="img" aria-label="Photo: paved courtyard with topiary and flower beds" x="0" y="372" width="340" height="200" fill="url(#tone-arbour)"/>
      <circle role="img" aria-label="Photo: clipped topiary ball" cx="282" cy="542" r="34" fill="url(#tone-stone)" stroke="var(--paper)" stroke-width="4"/>
    </svg>
    <div class="feature feature--upper">
      <h3 class="heading feature__title">Weddings</h3>
      <p class="copy">Marrowind &amp; Co Gardens is the most exquisite wedding setting imaginable, with an opportunity for stunning photographs and vows said beneath beautiful rose arbours.</p>
    </div>
    <div class="feature feature--lower">
      <h3 class="heading feature__title">The Marrowind Gardens</h3>
      <p class="copy">Every corner of the grounds has been lovingly and patiently developed over many years, from the sunken garden to the pond at the bottom of the hill. We look forward to welcoming you.</p>
    </div>
  </article>
</section>

</body>
</html>
```